Android app task management design

We have an android app that needs improvement in design. We have used a color pallet that we'd like to continue to use (attached). I have attached files of how the app is now, how someone else tried to improve the design (downloads file) and a report that also needs a redesign (the pdf). We'd like the design to be more modern, fresh and professional. The app is used by gas stations, hotels, restaurants and other companies that need HACCP registration because of food regulations. The app will be mostly used on tablets.
Target Market(s)
Gas stations, hotels, restaurants
Industry/Entity Type
Digital
Requirements
Must have
- A professional and clear user interface with a modern look that will last long. It must have colors from the color pallet attached.
Nice to have
- The fox attached. (Name: Tidy wren)

```html
<!DOCTYPE html>
<html lang="nl">
<head>
<meta charset="utf-8">
<title>Subtaak – takenlijst</title>
<link rel="stylesheet" href="https://fonts.googleapis.com/css2?family=Nunito+Sans:wght@400;600;700&display=swap">
<style>
  :root {
    --page-bg: #eef2f5;
    --screen-bg: #ffffff;
    --accent-blue: #3ec1f3;
    --link-blue: #29b6ee;
    --done-green: #1ee31e;
    --done-orange: #ff9a1a;
    --text-main: #5c5c5c;
    --text-muted: #a8a8a8;
    --title-grey: #a3a3a3;
    --divider: #e6e6e6;
    --ring-grey: #9b9b9b;
  }
  * { box-sizing: border-box; margin: 0; padding: 0; }
  html, body { width: 1200px; height: 1055px; overflow: hidden; }
  body {
    background: var(--page-bg);
    font-family: "Nunito Sans", sans-serif;
    position: relative;
  }
  .screen {
    position: absolute;
    top: 158px;
    width: 420px;
    height: 740px;
    background: var(--screen-bg);
    box-shadow: 0 10px 40px rgba(40, 70, 100, 0.12);
    overflow: hidden;
  }
  .screen--overview { left: 92px; }
  .screen--status { left: 688px; }

  .app-bar { position: absolute; top: 30px; left: 0; width: 100%; height: 28px; }
  .app-bar__menu { position: absolute; left: 29px; top: 7px; }
  .app-bar__title {
    position: absolute; left: 0; right: 0; top: 2px;
    text-align: center; font-weight: 700; font-size: 16px; color: var(--title-grey);
  }
  .app-bar__search { position: absolute; right: 36px; top: 4px; }

  .task-list { position: absolute; top: 82px; left: 0; width: 100%; list-style: none; }
  .task { position: relative; height: 83px; }
  .task::after {
    content: ""; position: absolute; left: 77px; right: 38px; bottom: 0;
    height: 1px; background: var(--divider);
  }
  .task:last-child::after { display: none; }
  .task__mark { position: absolute; left: 27px; top: 28px; width: 29px; height: 29px; }
  .task__name {
    position: absolute; left: 77px; top: 24px;
    font-size: 16px; color: var(--text-main); font-weight: 400;
  }
  .task__date {
    position: absolute; left: 77px; top: 47px;
    font-size: 9px; color: var(--text-main);
  }
  .task--done .task__name, .task--done .task__date { color: var(--done-orange); }
  .task__state {
    position: absolute; right: 38px; bottom: 5px;
    font-size: 10px; color: var(--text-muted);
  }

  .pager { position: absolute; top: 678px; left: 0; width: 100%; }
  .pill {
    position: absolute; top: -16px; height: 32px; border-radius: 16px;
    background: #fff; box-shadow: 0 6px 16px rgba(62, 193, 243, 0.12);
    font-size: 11px; font-weight: 700; color: var(--link-blue);
    display: flex; align-items: center; justify-content: center; gap: 12px;
  }
  .pill--back { left: 26px; width: 100px; }
  .pill--more { left: 270px; width: 100px; }
  .fab {
    position: absolute; left: 181px; top: -27px; width: 54px; height: 54px; border-radius: 50%;
    background: var(--accent-blue); box-shadow: 0 8px 18px rgba(62, 193, 243, 0.4);
    display: flex; align-items: center; justify-content: center;
  }
</style>
</head>
<body>

<section class="screen screen--overview">
  <header class="app-bar">
    <svg class="app-bar__menu" width="26" height="14" viewBox="0 0 26 14"><rect width="26" height="3.5" rx="1.75" fill="#3ec1f3"/><rect y="8" width="20" height="3.5" rx="1.75" fill="#3ec1f3"/></svg>
    <h1 class="app-bar__title">Subtaak</h1>
    <svg class="app-bar__search" width="16" height="16" viewBox="0 0 16 16"><circle cx="6.5" cy="6.5" r="4.6" fill="none" stroke="#3ec1f3" stroke-width="2.2"/><line x1="10" y1="10" x2="14.5" y2="14.5" stroke="#3ec1f3" stroke-width="2.6" stroke-linecap="round"/></svg>
  </header>
  <ul class="task-list">
    <li class="task task--done"><svg class="task__mark" viewBox="0 0 29 29"><circle cx="14.5" cy="14.5" r="14.5" fill="#1ee31e"/><path d="M8.5 15l4 4 8-8.5" fill="none" stroke="#fff" stroke-width="2.6" stroke-linecap="round" stroke-linejoin="round"/></svg><span class="task__name">koffieshop opruimen</span><span class="task__date">06.05.2018 3:05pm</span></li>
    <li class="task task--done"><svg class="task__mark" viewBox="0 0 29 29"><circle cx="14.5" cy="14.5" r="14.5" fill="#1ee31e"/><path d="M8.5 15l4 4 8-8.5" fill="none" stroke="#fff" stroke-width="2.6" stroke-linecap="round" stroke-linejoin="round"/></svg><span class="task__name">Toiletten Ochtend</span><span class="task__date">06.05.2018 3:09pm</span></li>
    <li class="task task--done"><svg class="task__mark" viewBox="0 0 29 29"><circle cx="14.5" cy="14.5" r="14.5" fill="#1ee31e"/><path d="M8.5 15l4 4 8-8.5" fill="none" stroke="#fff" stroke-width="2.6" stroke-linecap="round" stroke-linejoin="round"/></svg><span class="task__name">Koffietafel</span><span class="task__date">06.05.2018 3:55pm</span></li>
    <li class="task"><svg class="task__mark" viewBox="0 0 29 29"><circle cx="14.5" cy="14.5" r="13.3" fill="none" stroke="#9b9b9b" stroke-width="2.2"/></svg><span class="task__name">Stofzuigen En/Of vegen</span><span class="task__date">06.05.2018 4:05pm</span></li>
    <li class="task"><svg class="task__mark" viewBox="0 0 29 29"><circle cx="14.5" cy="14.5" r="13.3" fill="none" stroke="#9b9b9b" stroke-width="2.2"/></svg><span class="task__name">Vloeren Nat Reinigen</span><span class="task__date">06.05.2018 3:05pm</span></li>
    <li class="task"><svg class="task__mark" viewBox="0 0 29 29"><circle cx="14.5" cy="14.5" r="13.3" fill="none" stroke="#9b9b9b" stroke-width="2.2"/></svg><span class="task__name">Bakery Reinigen</span><span class="task__date">06.05.2018 3:05pm</span></li>
    <li class="task"><svg class="task__mark" viewBox="0 0 29 29"><circle cx="14.5" cy="14.5" r="13.3" fill="none" stroke="#9b9b9b" stroke-width="2.2"/></svg><span class="task__name">Statafel</span><span class="task__date">06.05.2018 3:05pm</span></li>
  </ul>
  <nav class="pager">
    <span class="pill pill--back"><svg width="11" height="8" viewBox="0 0 11 8"><path d="M10 4H1.5M4.5 1L1.5 4l3 3" fill="none" stroke="#b8b8b8" stroke-width="1.2" stroke-linecap="round"/></svg>Terug</span>
    <span class="fab"><svg width="26" height="18" viewBox="0 0 26 18"><rect width="26" height="2.6" rx="1.3" fill="#fff"/><rect x="6" y="7" width="14" height="2.6" rx="1.3" fill="#fff"/><rect x="10.5" y="14" width="5" height="2.6" rx="1.3" fill="#fff"/></svg></span>
    <span class="pill pill--more">Meer laden...</span>
  </nav>
</section>

<section class="screen screen--status">
  <header class="app-bar">
    <svg class="app-bar__menu" width="26" height="14" viewBox="0 0 26 14"><rect width="26" height="3.5" rx="1.75" fill="#3ec1f3"/><rect y="8" width="20" height="3.5" rx="1.75" fill="#3ec1f3"/></svg>
    <h1 class="app-bar__title">Subtaak</h1>
    <svg class="app-bar__search" width="16" height="16" viewBox="0 0 16 16"><circle cx="6.5" cy="6.5" r="4.6" fill="none" stroke="#3ec1f3" stroke-width="2.2"/><line x1="10" y1="10" x2="14.5" y2="14.5" stroke="#3ec1f3" stroke-width="2.6" stroke-linecap="round"/></svg>
  </header>
  <ul class="task-list">
    <li class="task task--done"><svg class="task__mark" viewBox="0 0 29 29"><circle cx="14.5" cy="14.5" r="14.5" fill="#1ee31e"/><path d="M8.5 15l4 4 8-8.5" fill="none" stroke="#fff" stroke-width="2.6" stroke-linecap="round" stroke-linejoin="round"/></svg><span class="task__name">koffieshop opruimen</span><span class="task__date">06.05.2018 3:05pm</span><span class="task__state">voltooid</span></li>
    <li class="task task--done"><svg class="task__mark" viewBox="0 0 29 29"><circle cx="14.5" cy="14.5" r="14.5" fill="#1ee31e"/><path d="M8.5 15l4 4 8-8.5" fill="none" stroke="#fff" stroke-width="2.6" stroke-linecap="round" stroke-linejoin="round"/></svg><span class="task__name">Toiletten Ochtend</span><span class="task__date">06.05.2018 3:09pm</span><span class="task__state">voltooid</span></li>
    <li class="task task--done"><svg class="task__mark" viewBox="0 0 29 29"><circle cx="14.5" cy="14.5" r="14.5" fill="#1ee31e"/><path d="M8.5 15l4 4 8-8.5" fill="none" stroke="#fff" stroke-width="2.6" stroke-linecap="round" stroke-linejoin="round"/></svg><span class="task__name">Koffietafel</span><span class="task__date">06.05.2018 3:55pm</span><span class="task__state">voltooid</span></li>
    <li class="task"><svg class="task__mark" viewBox="0 0 29 29"><circle cx="14.5" cy="14.5" r="13.3" fill="none" stroke="#9b9b9b" stroke-width="2.2"/></svg><span class="task__name">Stofzuigen En/Of vegen</span><span class="task__date">06.05.2018 4:05pm</span><span class="task__state">niet compleet</span></li>
    <li class="task"><svg class="task__mark" viewBox="0 0 29 29"><circle cx="14.5" cy="14.5" r="13.3" fill="none" stroke="#9b9b9b" stroke-width="2.2"/></svg><span class="task__name">Vloeren Nat Reinigen</span><span class="task__date">06.05.2018 3:05pm</span><span class="task__state">niet compleet</span></li>
    <li class="task"><svg class="task__mark" viewBox="0 0 29 29"><circle cx="14.5" cy="14.5" r="13.3" fill="none" stroke="#9b9b9b" stroke-width="2.2"/></svg><span class="task__name">Bakery Reinigen</span><span class="task__date">06.05.2018 3:05pm</span><span class="task__state">niet compleet</span></li>
    <li class="task"><svg class="task__mark" viewBox="0 0 29 29"><circle cx="14.5" cy="14.5" r="13.3" fill="none" stroke="#9b9b9b" stroke-width="2.2"/></svg><span class="task__name">Statafel</span><span class="task__date">06.05.2018 3:05pm</span></li>
  </ul>
  <nav class="pager">
    <span class="pill pill--back"><svg width="11" height="8" viewBox="0 0 11 8"><path d="M10 4H1.5M4.5 1L1.5 4l3 3" fill="none" stroke="#b8b8b8" stroke-width="1.2" stroke-linecap="round"/></svg>Terug</span>
    <span class="fab"><svg width="26" height="18" viewBox="0 0 26 18"><rect width="26" height="2.6" rx="1.3" fill="#fff"/><rect x="6" y="7" width="14" height="2.6" rx="1.3" fill="#fff"/><rect x="10.5" y="14" width="5" height="2.6" rx="1.3" fill="#fff"/></svg></span>
    <span class="pill pill--more">Meer laden...</span>
  </nav>
</section>

</body>
</html>
```